Business cards for KORU Real Estate Holdings LLC

We need a cool, original business card design for a company based in the Washington DC metropolitan area. We are a new energetic and passionate Real Estate Investing Company that invests in all types of real estate; commercial, residential, industrial etc.

Our company color is Red since it reflects action, energy and speed; it is assertive confident, energizing, exciting, powerful, passionate and determined. So we would like business card communicate those qualities to the audience.

Our audiences are investors that want to invest with us, real estate sellers, buyers, and tenants who lease from us.

Our logo is attached

```html
<!DOCTYPE html>
<html lang="en">
<head>
<meta charset="utf-8">
<title>KORU Real Estate Holdings LLC — Business Cards</title>
<link rel="stylesheet" href="https://fonts.googleapis.com/css2?family=Saira+Semi+Condensed:wght@700&family=Arimo:wght@400&display=swap">
<style>
  :root {
    --backdrop: #b9b9b9;
    --card-red: #dc1f26;
    --strip-white: #ffffff;
    --ink-dark: #2a2a2a;
    --ink-soft: #1e1e1e;
    --divider: #3a3a3a;
  }
  * { margin: 0; padding: 0; box-sizing: border-box; }
  html, body { width: 1200px; height: 960px; overflow: hidden; }
  body {
    position: relative;
    background: var(--backdrop);
    font-family: "Arimo", Arial, sans-serif;
  }
  .card {
    position: absolute;
    width: 702px;
    height: 406px;
    background: var(--card-red);
    overflow: hidden;
  }
  .card--front { left: 174px; top: 38px; }
  .card--back { left: 420px; top: 480px; }

  .front-strip {
    position: absolute;
    left: 96px; top: 0;
    width: 126px; height: 100%;
    background: var(--strip-white);
  }
  .brand-dot {
    position: absolute;
    background: var(--ink-dark);
    border-radius: 50%;
  }
  .card--front .brand-dot { left: 124px; top: 200px; width: 70px; height: 70px; }
  .front-website {
    position: absolute;
    left: 96px; top: 342px;
    width: 160px;
    font-size: 10.5px;
    color: var(--ink-soft);
  }

  .wordmark {
    position: absolute;
    font-family: "Saira Semi Condensed", "Arial Narrow", sans-serif;
    font-weight: 700;
    color: var(--ink-dark);
    line-height: 1;
  }
  .wordmark__name { display: block; letter-spacing: 2px; }
  .wordmark__line { display: block; }
  .card--front .wordmark { left: 226px; top: 178px; }
  .card--front .wordmark__name { font-size: 96px; }
  .card--front .wordmark__line { font-size: 25px; margin-top: -2px; letter-spacing: 0.5px; }

  .card--back .brand-dot { left: 72px; top: 172px; width: 52px; height: 52px; }
  .card--back .wordmark { left: 134px; top: 156px; }
  .card--back .wordmark__name { font-size: 64px; }
  .card--back .wordmark__line { font-size: 17px; letter-spacing: 0.4px; }

  .back-divider {
    position: absolute;
    left: 398px; top: 70px;
    width: 2px; height: 230px;
    background: var(--divider);
  }
  .contact-list {
    position: absolute;
    left: 420px; top: 92px;
    list-style: none;
  }
  .contact-list li {
    display: flex;
    align-items: center;
    height: 27px;
    font-size: 15px;
    color: var(--ink-soft);
  }
  .contact-list svg {
    width: 16px; height: 16px;
    margin-right: 14px;
    fill: var(--ink-soft);
    flex: none;
  }
</style>
</head>
<body>

<section class="card card--front" aria-label="Business card front">
  <div class="front-strip"></div>
  <span class="brand-dot"></span>
  <h1 class="wordmark">
    <span class="wordmark__name">KORU</span>
    <span class="wordmark__line">REAL ESTATE HOLDINGS LLC</span>
  </h1>
  <p class="front-website">www.koruholdings.com</p>
</section>

<section class="card card--back" aria-label="Business card back">
  <span class="brand-dot"></span>
  <h2 class="wordmark">
    <span class="wordmark__name">KORU</span>
    <span class="wordmark__line">REAL ESTATE HOLDINGS LLC</span>
  </h2>
  <div class="back-divider"></div>
  <ul class="contact-list">
    <li>
      <svg viewBox="0 0 16 16" aria-hidden="true"><path d="M4 0h8a1 1 0 0 1 1 1v14a1 1 0 0 1-1 1H4a1 1 0 0 1-1-1V1a1 1 0 0 1 1-1zm1 2v10h6V2zm3 11a1 1 0 1 0 0 2 1 1 0 0 0 0-2z"/></svg>
      55 5555 5555
    </li>
    <li>
      <svg viewBox="0 0 16 16" aria-hidden="true"><path d="M1 5c2-3 12-3 14 0l-1 2-3-1V4H5v2L2 7zM3 9h10l1 5H2zm5 1.5a1.5 1.5 0 1 0 0 3 1.5 1.5 0 0 0 0-3z"/></svg>
      44 4444 4444
    </li>
    <li>
      <svg viewBox="0 0 16 16" aria-hidden="true"><path d="M1 3h14v1L8 9 1 4zm0 3l7 5 7-5v7H1z"/></svg>
      info@koruholdings.com
    </li>
    <li>
      <svg viewBox="0 0 16 16" aria-hidden="true"><path d="M8 0a8 8 0 1 0 0 16A8 8 0 0 0 8 0zm0 1.5c.9 0 2 1.9 2.3 5H5.7C6 3.4 7.1 1.5 8 1.5zM1.6 6.5h2.6A15 15 0 0 1 5 2.2 6.5 6.5 0 0 0 1.6 6.5zm9.4-4.3a15 15 0 0 1 .8 4.3h2.6A6.5 6.5 0 0 0 11 2.2zM1.6 9.5A6.5 6.5 0 0 0 5 13.8a15 15 0 0 1-.8-4.3zm4.1 0c.3 3.1 1.4 5 2.3 5s2-1.9 2.3-5zm6.1 0a15 15 0 0 1-.8 4.3 6.5 6.5 0 0 0 3.4-4.3z"/></svg>
      www.koruholdings.com
    </li>
    <li>
      <svg viewBox="0 0 16 16" aria-hidden="true"><path d="M8 0a5.5 5.5 0 0 0-5.5 5.5C2.5 10 8 16 8 16s5.5-6 5.5-10.5A5.5 5.5 0 0 0 8 0zm0 3.5a2 2 0 1 1 0 4 2 2 0 0 1 0-4z"/></svg>
      area,state,zipcode,country
    </li>
  </ul>
</section>

</body>
</html>
```